Business Card *

A business card design
Use the logo uploaded in the brief page.
You may use placeholders in your design layouts.
I will provide the actual business card details to the winning designer.

Logo
Place for contact info (name, title, phone, email, etc)

Requirements
Must have
• Logo

```html
<!DOCTYPE html>
<html lang="en">
<head>
<meta charset="utf-8">
<title>Fieldgear Business Card</title>
<link rel="stylesheet" href="https://fonts.googleapis.com/css2?family=Roboto:wght@400;700&display=swap">
<style>
  :root {
    --stage: #dcdcda;
    --card: #1b1b1b;
    --card-deep: #121212;
    --green: #3cc24a;
    --lime: #8fd63a;
    --silver: #b9b9b9;
    --text: #d6d6d6;
  }
  * { box-sizing: border-box; margin: 0; padding: 0; }
  html, body { width: 1200px; height: 801px; overflow: hidden; }
  body {
    background: var(--stage);
    font-family: "Roboto", Arial, sans-serif;
    display: flex;
    align-items: center;
    justify-content: center;
    gap: 40px;
  }
  .card {
    position: relative;
    width: 520px;
    height: 297px;
    background: var(--card);
    border-bottom: 3px solid var(--green);
    box-shadow: 0 10px 24px rgba(0,0,0,.25);
    overflow: hidden;
  }
  /* front */
  .card-front { display: flex; align-items: center; }
  .brand-block {
    width: 250px;
    display: flex;
    align-items: center;
    justify-content: center;
    gap: 10px;
  }
  .brand-dot {
    width: 26px; height: 26px;
    border-radius: 50%;
    background: var(--green);
  }
  .brand-name {
    font-weight: 700;
    font-size: 30px;
    letter-spacing: 1px;
    color: var(--silver);
    text-transform: uppercase;
  }
  .divider {
    width: 1px;
    height: 170px;
    background: var(--lime);
  }
  .contact {
    padding-left: 26px;
    color: var(--text);
    font-size: 14px;
    line-height: 1.45;
  }
  .contact-name {
    color: var(--green);
    font-weight: 700;
    font-size: 19px;
    letter-spacing: .5px;
    text-transform: uppercase;
  }
  .contact-title { margin-bottom: 8px; }
  .contact-address { margin-bottom: 6px; }
  .contact-line { display: flex; align-items: center; gap: 8px; }
  .contact-line svg { width: 13px; height: 13px; flex: none; }
  .web-accent { color: var(--green); }
  /* back */
  .back-pattern {
    position: absolute; inset: 0;
    background: linear-gradient(120deg, #4a4a4a 0%, #2a2a2a 40%, var(--card-deep) 100%);
  }
  .back-brand {
    position: absolute;
    right: 70px; top: 50%;
    transform: translateY(-50%);
    display: flex; align-items: center; gap: 8px;
  }
  .back-brand .brand-name { font-size: 20px; }
  .back-brand .brand-dot { width: 18px; height: 18px; }
</style>
</head>
<body>
  <section class="card card-front">
    <div class="brand-block">
      <span class="brand-dot"></span>
      <span class="brand-name">Fieldgear</span>
    </div>
    <div class="divider"></div>
    <div class="contact">
      <p class="contact-name">Marcus Ellery</p>
      <p class="contact-title">Managing Director</p>
      <p class="contact-address">Alder Ridge Avenue,<br>Suite 210 Harbor Point</p>
      <p class="contact-line">
        <svg viewBox="0 0 16 16"><rect x="1" y="1" width="14" height="14" rx="3" fill="var(--green)"/><path d="M5 4h2l1 2-1.5 1a6 6 0 0 0 2.5 2.5L10 8l2 1v2a1 1 0 0 1-1 1A8 8 0 0 1 4 5a1 1 0 0 1 1-1z" fill="#1b1b1b"/></svg>
        555.014.2270
      </p>
      <p class="contact-line">
        <svg viewBox="0 0 16 16"><rect x="1" y="3" width="14" height="10" fill="var(--green)"/><path d="M1 3l7 6 7-6" fill="none" stroke="#1b1b1b" stroke-width="1.2"/></svg>
        marcus@fieldgear.com
      </p>
      <p class="contact-line">
        <svg viewBox="0 0 16 16"><circle cx="8" cy="8" r="7" fill="var(--green)"/><path d="M1 8h14M8 1c-3 3-3 11 0 14M8 1c3 3 3 11 0 14" fill="none" stroke="#1b1b1b" stroke-width="1"/></svg>
        www.<span class="web-accent">fieldgear</span>.com
      </p>
    </div>
  </section>

  <section class="card card-back">
    <div class="back-pattern" role="img" aria-label="Repeating embossed brand pattern in glossy black"></div>
    <div class="back-brand">
      <span class="brand-dot"></span>
      <span class="brand-name">Fieldgear</span>
    </div>
  </section>
</body>
</html>
```